Design clean technology service-based company website

Hello, We are looking to reskin our company website. We are an environmental inspection company and test for Asbestos, Lead and Mold along with other contaminants. People depend on the results to be accurate and fast. We are regulated by the NQB and State regulations. We work a lot with business to business and business to customer. We are wanting to make our new presentation to be modern and easy for customers to interact with us, understand our process and services while providing valuable environmental informational resource and updates. We are a technology based company and will be providing instantaneous results as reports come in for the customers. We are needing good calls to action on the site to direct them to setup a new inspection. Each user will have a backend access to their job information with invoices, reports, status, etc. We have developed software to be able to proved these reports and want to look the part.

My current website is www.trylumaverde.com
Updates

Helllo we are wanting to make sure we have good time to select the right website for us and also have the additional time to select other pages of the website. We have received great designs and have consolidated our requests into a document for the next set of iterations.

Target Market(s)

Home Owners, Contractors, Engineers, Real Estate Agents, Building Owners, Insurance Adjusters

Industry/Entity Type

Environmental Consultant

Number of Pages Required

5+ page

Font styles to use
Sans Serif

Colors
0355a3
9bcb3c
7f7f7f
f5f5f5
000000

Requirements
Must have
• Use our existing logo to design around
• The layouts look good in mobile mode for understanding and selecting services and signing up
• Clean Modern Layout
• Have all pages on the website have a similar layout and feel
• Clearly communicate services along with bundle service packages
• Detail the customer journey with graphic design
• Great call to actions to either schedule inspection online, call, text, chat
Nice to have
• Have an interactive graphic for where to test for lead, asbestos and mold.
• I like the becky barlows top order line bar - see attached
• Have clear question and answer page layouts for asbestos, lead and mold
• Show Company reviews
• Have clear Resources pages for all types of contaminants
Should not have
• My current website is www.trylumaverde.com

```html
<!DOCTYPE html>
<html lang="en">
<head>
<meta charset="utf-8">
<title>LumaVerde Environmental Inspections</title>
<link rel="stylesheet" href="https://fonts.googleapis.com/css2?family=Barlow:wght@400;500;600;700&display=swap">
<style>
:root{
  --green:#9bcb3c;
  --grey:#7f7f7f;
  --light:#f5f5f5;
  --ink:#000000;
  --dark:#1f1f1f;
  --white:#ffffff;
}
*{box-sizing:border-box;margin:0;padding:0}
html,body{width:1200px;height:1200px;overflow:hidden;background:var(--white);font-family:"Barlow",Arial,sans-serif}
.page{position:relative;width:1200px;height:1200px}
.site-header{position:absolute;left:0;top:0;width:1200px;height:75px;background:var(--white);border-bottom:1px solid #e2e2e2}
.brand{position:absolute;left:53px;top:22px;display:flex;align-items:center;gap:6px;font-size:25px;font-weight:600;color:var(--green);letter-spacing:.5px}
.brand-dot{width:10px;height:10px;border-radius:50%;background:var(--green)}
.main-nav{position:absolute;top:31px;left:0;font-size:10px;font-weight:500;color:var(--ink)}
.main-nav span{position:absolute;white-space:nowrap}
.account-link{position:absolute;left:951px;top:31px;font-size:10px;color:var(--green);white-space:nowrap}
.sign-in{position:absolute;left:1071px;top:26px;width:76px;height:23px;border:1.5px solid var(--green);border-radius:3px;color:var(--green);font-size:10px;display:flex;align-items:center;justify-content:center}
.hero{position:absolute;left:0;top:75px;width:1200px;height:472px;background:linear-gradient(100deg,#1f1f1f 0%,#222 45%,#5a5a5a 65%,#8a8a8a 80%,#4a4a4a 100%)}
.hero-title{position:absolute;left:234px;top:120px;font-size:47px;font-weight:700;color:var(--white);letter-spacing:1px}
.hero-copy{position:absolute;left:234px;top:181px;width:370px;font-size:15px;line-height:18px;font-weight:500;color:var(--white)}
.hero-cta{position:absolute;left:234px;top:274px;width:196px;height:32px;border:1.5px solid var(--green);border-radius:2px;color:var(--green);font-size:16px;font-weight:600;letter-spacing:1.5px;display:flex;align-items:center;justify-content:center}
.hero-phone{position:absolute;left:234px;top:326px;display:flex;align-items:center;gap:8px;color:var(--white);font-size:20px;font-weight:500;letter-spacing:1.5px}
.slider-dots{position:absolute;left:560px;top:434px;display:flex;gap:7px}
.slider-dots i{display:block;width:22px;height:3px;background:#bdbdbd}
.slider-dots i.active{background:var(--green)}
.intro{position:absolute;left:0;top:604px;width:1200px;text-align:center}
.intro h2{font-size:23px;font-weight:500;letter-spacing:3px;color:var(--grey)}
.accent{color:var(--green)}
.intro p{margin:20px auto 0;width:340px;font-size:11px;line-height:13px;letter-spacing:1px;color:var(--grey)}
.call-btn{position:absolute;left:508px;top:717px;width:185px;height:26px;background:var(--green);color:var(--white);font-size:10.5px;font-weight:600;letter-spacing:1.2px;display:flex;align-items:center;justify-content:center;border-radius:2px;box-shadow:0 2px 6px rgba(0,0,0,.15)}
.globe-art{position:absolute;left:528px;top:804px;width:146px;height:152px;border-radius:50%;background:radial-gradient(circle at 50% 50%,var(--green) 0 42%,#f0f1f3 43% 70%,var(--white) 71%)}
.services{position:absolute;left:0;top:992px;width:1200px;text-align:center}
.services h2{font-size:55px;font-weight:700;color:var(--grey);letter-spacing:1px;line-height:60px}
.services p{margin:20px auto 0;width:500px;font-size:11px;line-height:13px;letter-spacing:1px;color:var(--grey)}
.service-tabs{position:absolute;left:234px;top:1143px;width:732px;height:33px;background:var(--green);border-radius:2px;display:flex;align-items:center;color:var(--white);font-size:11px;font-weight:600}
.service-tabs span{flex:1;text-align:center}
.service-tabs b{width:1.5px;height:16px;background:var(--white)}
</style>
</head>
<body>
<div class="page">
  <header class="site-header">
    <div class="brand"><span class="brand-dot"></span>LumaVerde</div>
    <nav class="main-nav">
      <span style="left:350px">HOME</span>
      <span style="left:408px">OUR SERVICES</span>
      <span style="left:511px">RESOURCES</span>
      <span style="left:601px">BLOG</span>
      <span style="left:663px">Q &amp; A</span>
      <span style="left:729px">REVIEWS</span>
      <span style="left:804px">CONNECT</span>
    </nav>
    <span class="account-link">CREATE AN ACCOUNT</span>
    <span class="sign-in">SIGN IN</span>
  </header>

  <section class="hero" role="img" aria-label="Magnified black and white microscope photo of asbestos fibres">
    <h1 class="hero-title">ASBESTOS</h1>
    <p class="hero-copy">Lorem ipsum dolor sit amet, consectetuer adipiscing elit. Aenean commodo ligula eget dolor. Aenean massa. Cum sociis natoque penatibus et magnis dis parturient montes, nascetur ridiculus mus...</p>
    <div class="hero-cta">ASBESTOS TESTING</div>
    <div class="hero-phone">
      <svg width="14" height="18" viewBox="0 0 14 18"><path d="M3 1 L6 1 L7 5 L5 6.5 C5.5 9 7 11.5 9 13 L11 12 L13.5 14.5 L12 17 C6 17 1 10 1 4 Z" fill="#fff"/></svg>
      555 014 2290
    </div>
    <div class="slider-dots"><i></i><i class="active"></i><i></i></div>
  </section>

  <section class="intro">
    <h2>NEW <span class="accent">CONSTRUCTION</span> PROJECT?</h2>
    <p>Let us start you in the right direction with our certified asbestos inspections. Residential, commercial, schools, governmental properties, multi-family and more.</p>
  </section>
  <div class="call-btn">CALL NOW: 555 014 2290</div>

  <div class="globe-art" role="img" aria-label="Green globe illustration with a pie chart badge"></div>

  <section class="services">
    <h2>OUR <span class="accent">SERVICES</span></h2>
    <p>Nulla consequat massa quis enim. Donec pede justo, fringilla vel, aliquet nec, vulputate eget, arcu.material. In the state of colorado you must check for, asbestos according to SEHB (State Environmental Health Board.</p>
  </section>
  <nav class="service-tabs">
    <span>COMMERCIAL SERVICES</span><b></b>
    <span>RESIDENTIAL SERVICES</span><b></b>
    <span>HOMEOWNER &amp; CONTRACTER SERVICES</span>
  </nav>
</div>
</body>
</html>
```